Need Help having my business card stand out

I am the owner of Brisa Canine Coaching and would like for my business cards to stand out. I have been trying to keep designing them myself but I can't get what I have in my head on the card. I will try my best to post templates that I like for inspirations. I want something unique but elegant. I don't want in to look cartoony or cheesy. It needs to pop in a pet shop but also in a coffee shop or gym.

Target Market(s)

Dog owners, Married ,No young kids Jr High school kids and up (maybe kids on the way) Executives, Stay at home moms/wives, Small business owners

Industry/Entity Type

Dog Training

Contact Information for Business Card

Lorna Whitfield, 555-304-7719, info@brisacanine.example, www.brisacanine.example

Colors

Designer to choose colors to be used in the design.

Requirements
Must have
• my logo
Should not have
• Cursive lettering

```html
<!DOCTYPE html>
<html lang="en">
<head>
<meta charset="utf-8">
<title>Brisa Canine Coaching – Business Card</title>
<link href="https://fonts.googleapis.com/css2?family=Open+Sans:wght@400;700&family=Quicksand:wght@400;500&display=swap" rel="stylesheet">
<style>
  :root {
    --bg: #1a63b8;
    --navy: #14427f;
    --deep: #0f3a78;
    --brand: #1e5fb0;
    --accent: #3b8de0;
    --sky: #4aa3ea;
    --band: #ececec;
    --ink: #2a2a2a;
    --muted: #5b5b5b;
    --white: #ffffff;
  }
  * { box-sizing: border-box; margin: 0; padding: 0; }
  html, body { width: 1200px; height: 856px; overflow: hidden; }
  body {
    background: var(--bg);
    font-family: "Open Sans", Arial, sans-serif;
    position: relative;
  }
  .card {
    position: absolute;
    top: 280px;
    width: 520px;
    height: 297px;
    border-radius: 28px;
    overflow: hidden;
    box-shadow: 0 12px 30px rgba(0, 20, 60, .35);
  }
  /* Front */
  .card-front { left: 50px; background: var(--white); }
  .front-band {
    position: absolute; left: 0; right: 0; top: 62px; height: 52px;
    background: var(--band);
  }
  .brand-mark {
    position: absolute; right: 30px; top: 28px;
    display: flex; align-items: center; gap: 8px;
  }
  .brand-mark .dot { width: 12px; height: 12px; background: var(--navy); }
  .brand-mark .name {
    font-weight: 700; font-size: 20px; color: var(--navy); letter-spacing: .2px;
  }
  .holder { position: absolute; left: 34px; top: 114px; }
  .holder .person { font-weight: 700; font-size: 19px; line-height: 26px; color: var(--brand); }
  .holder .role { font-size: 13px; line-height: 18px; color: var(--muted); }
  .rule {
    position: absolute; left: 150px; right: 60px; top: 148px;
    height: 1px; background: var(--ink);
  }
  .rule::after {
    content: ""; position: absolute; right: -6px; top: -3px;
    width: 6px; height: 6px; background: var(--accent);
  }
  .contact {
    position: absolute; left: 215px; top: 156px;
    font-size: 10.5px; color: var(--muted); line-height: 1.9;
  }
  .contact .row { display: flex; align-items: center; gap: 6px; }
  .contact svg { width: 10px; height: 10px; fill: var(--muted); flex: none; }
  .contact .sep { width: 10px; }
  .front-base {
    position: absolute; left: 0; right: 0; bottom: 0; height: 64px;
    background: linear-gradient(90deg, var(--brand), var(--sky));
  }
  .commands {
    position: absolute; left: 160px; right: 0; bottom: 28px; height: 46px;
    background: var(--white); border-radius: 22px 0 0 22px;
    display: flex; align-items: center; gap: 12px; padding-left: 24px;
    font-family: "Quicksand", Arial, sans-serif; font-size: 17px; color: var(--accent);
    white-space: nowrap;
  }
  .commands span::before {
    content: ""; display: inline-block; margin-right: 7px;
    border-left: 6px solid var(--navy);
    border-top: 4px solid transparent; border-bottom: 4px solid transparent;
    vertical-align: middle;
  }
  /* Back */
  .card-back {
    left: 630px;
    background: linear-gradient(135deg, var(--deep) 0%, var(--brand) 55%, var(--sky) 100%);
  }
  .back-pattern {
    position: absolute; inset: 0;
    background: linear-gradient(160deg, rgba(255,255,255,.06), rgba(74,163,234,.25) 60%, rgba(15,58,120,.1));
  }
  .back-brand {
    position: absolute; left: 0; right: 0; top: 112px;
    display: flex; justify-content: center; align-items: center; gap: 10px;
  }
  .back-brand .dot { width: 14px; height: 14px; background: var(--deep); }
  .back-brand .name { font-weight: 700; font-size: 26px; color: var(--deep); }
  .web-tab {
    position: absolute; right: 0; bottom: 0; width: 300px; height: 40px;
    background: var(--accent); border-radius: 14px 0 0 0;
    display: flex; align-items: center; justify-content: center;
    color: var(--white); font-weight: 700; font-size: 14px;
  }
</style>
</head>
<body>
  <section class="card card-front" aria-label="Business card front">
    <div class="front-band"></div>
    <div class="brand-mark"><span class="dot"></span><span class="name">Brisa Canine Coaching</span></div>
    <div class="holder">
      <p class="person">Lorna Whitfield</p>
      <p class="role">Founder</p>
    </div>
    <div class="rule"></div>
    <div class="contact">
      <p class="row">
        <svg viewBox="0 0 10 10"><path d="M5 0a3.5 3.5 0 0 0-3.5 3.5C1.5 6 5 10 5 10s3.5-4 3.5-6.5A3.5 3.5 0 0 0 5 0zm0 5a1.5 1.5 0 1 1 0-3 1.5 1.5 0 0 1 0 3z"/></svg>
        #42 Harbor Lane, Westbrook, Victoria, 3100, Australia
      </p>
      <p class="row">
        <svg viewBox="0 0 10 10"><path d="M2 0l2 2.5-1 1.2a6 6 0 0 0 3.3 3.3l1.2-1L10 8l-1.5 2C4 10 0 6 0 1.5z"/></svg>
        555-304-7719
        <span class="sep"></span>
        <svg viewBox="0 0 10 10"><path d="M0 2h10v6H0z M0 2l5 3.5L10 2" stroke="#fff" stroke-width=".8"/></svg>
        info@brisacanine.example
      </p>
    </div>
    <div class="front-base"></div>
    <div class="commands"><span>come</span><span>sit</span><span>down</span><span>stay</span><span>good</span></div>
  </section>

  <section class="card card-back" aria-label="Business card back">
    <div class="back-pattern" role="img" aria-label="Abstract flowing blue light shapes"></div>
    <div class="back-brand"><span class="dot"></span><span class="name">Brisa Canine Coaching</span></div>
    <div class="web-tab">www.brisacanine.example</div>
  </section>
</body>
</html>
```